Dalwin Tasker Construction LLC

I like to have a business card the is unique, very professional and the it will projected the best first impression of me and my company

Target Market(s)

Remodeling, new constitution

Industry/Entity Type

Business

Font styles to use
Script

Requirements
Must have
• My company name email and phone number
Nice to have
• A logo maybe

```html
<!DOCTYPE html>
<html lang="en">
<head>
<meta charset="utf-8">
<title>Dalwin Tasker Construction LLC – Business Card</title>
<link rel="stylesheet" href="https://fonts.googleapis.com/css2?family=Arimo:wght@400;700&display=swap">
<style>
  :root {
    --stage: #1b1b1b;
    --card-red: #a92126;
    --card-white: #f4f4f4;
    --ink: #111111;
    --ink-soft: #2a2a2a;
    --paper-text: #ffffff;
    --mark-faint: #eadfe0;
  }
  * { margin: 0; padding: 0; box-sizing: border-box; }
  html, body {
    width: 1200px;
    height: 800px;
    overflow: hidden;
    background: var(--stage);
    font-family: "Arimo", Arial, sans-serif;
  }
  .stage {
    position: relative;
    width: 1200px;
    height: 800px;
  }
  .card {
    position: absolute;
    top: 252px;
    width: 520px;
    height: 297px;
    box-shadow: 0 18px 40px rgba(0,0,0,0.55);
  }
  .card--front {
    left: 50px;
    background: var(--card-red);
    display: flex;
    align-items: center;
    justify-content: center;
  }
  .card--back {
    left: 630px;
    background: var(--card-white);
  }
  .brand {
    display: flex;
    align-items: center;
    gap: 14px;
    color: var(--paper-text);
  }
  .brand__square {
    width: 44px;
    height: 44px;
    background: var(--paper-text);
  }
  .brand__name {
    font-weight: 400;
    font-size: 24px;
    line-height: 1.2;
    color: var(--paper-text);
  }
  .holder {
    position: absolute;
    left: 34px;
    top: 30px;
  }
  .holder__name {
    font-weight: 700;
    font-size: 16px;
    color: var(--ink);
  }
  .holder__title {
    font-weight: 400;
    font-size: 12px;
    color: var(--ink-soft);
    margin-top: 2px;
  }
  .back-mark {
    position: absolute;
    left: 50%;
    top: 50%;
    width: 84px;
    height: 84px;
    transform: translate(-50%, -50%);
    background: var(--mark-faint);
  }
  .contact {
    position: absolute;
    right: 34px;
    bottom: 30px;
    text-align: right;
    font-size: 14px;
    line-height: 1.35;
    color: var(--ink);
  }
</style>
</head>
<body>
  <main class="stage">
    <section class="card card--front" aria-label="Card front">
      <div class="brand">
        <span class="brand__square" aria-hidden="true"></span>
        <span class="brand__name">Dalwin Tasker Construction LLC</span>
      </div>
    </section>

    <section class="card card--back" aria-label="Card back">
      <div class="holder">
        <p class="holder__name">Your Name goes here</p>
        <p class="holder__title">Your Title goes here</p>
      </div>
      <span class="back-mark" aria-hidden="true"></span>
      <div class="contact">
        <p>p: 0198765432</p>
        <p>e: name@taskerbuild.com</p>
      </div>
    </section>
  </main>
</body>
</html>
```